We require a business card that promotes our Electrical business. Things we would like included are;
1) our business name, Bright Path Electrical and Communication
2) Our Electrical licence, EC 27036
3) Our ABN, 52 147 906 318
4) Our website, www.ridgewirecrew.com.au
5) Our Email, info@ridgewirecrew.com.au
6) Our contact number, 0452 681 207
7) Our address, 48 Marlow Rd Tandridge Perth 6093
8) Our logo, I will attach this (can you please change it so the ackground is white not black)
9) Our colours are red and white and perhaps some black
10) Managing Director Dorian Velcourt
11) the back to say 'notes' and have some lines for writing

Target Market(s)

General

Industry/Entity Type

Electrical

Contact Information for Business Card

Include the colour white, black and red.

Font styles to use
Sans Serif

Requirements
Nice to have
• A thunder bolt or a power point or a cord or something electrical, cartoon image of a cartoon like electrical tradie

```html
<!DOCTYPE html>
<html lang="en">
<head>
<meta charset="utf-8">
<title>Bright Path Electrical &amp; Communication – Business Card</title>
<link rel="stylesheet" href="https://fonts.googleapis.com/css2?family=Lato:wght@400;700;900&display=swap">
<style>
  :root {
    --stage: #1b1b1b;
    --card-top: #2c2c2c;
    --card-bottom: #1e1e1e;
    --red: #e11b22;
    --white: #f2f2f2;
    --grey: #9a9a9a;
    --dots: #8c8c8c;
  }
  * { box-sizing: border-box; margin: 0; padding: 0; }
  html, body { width: 1200px; height: 873px; overflow: hidden; }
  body {
    background: var(--stage);
    font-family: "Lato", sans-serif;
    color: var(--white);
    display: flex;
    align-items: center;
    justify-content: center;
    gap: 40px;
  }
  .card {
    position: relative;
    width: 540px;
    height: 310px;
    border-radius: 16px;
    background: linear-gradient(150deg, var(--card-top), var(--card-bottom));
    box-shadow: 0 10px 30px rgba(0,0,0,.55);
    overflow: hidden;
  }

  /* Front */
  .brand { position: absolute; left: 44px; top: 56px; display: flex; align-items: center; gap: 14px; }
  .brand-dot { width: 20px; height: 20px; border-radius: 50%; background: var(--red); flex: none; }
  .brand-name { font-weight: 700; font-size: 22px; line-height: 1.15; color: var(--white); }
  .tagline {
    position: absolute; left: 78px; top: 116px;
    font-size: 10.5px; font-style: italic; color: var(--grey);
    padding-top: 5px; border-top: 2px solid var(--red); width: 290px;
  }
  .person { position: absolute; right: 36px; top: 156px; text-align: right; }
  .person-name { color: var(--red); font-weight: 700; font-size: 17px; }
  .person-role { font-size: 11.5px; font-weight: 700; letter-spacing: .3px; margin-top: 3px; }
  .licence { color: var(--red); font-weight: 700; font-size: 13px; margin-top: 4px; }
  .abn { color: var(--white); font-weight: 400; font-size: 12px; margin-top: 3px; }
  .contacts { position: absolute; left: 36px; bottom: 26px; list-style: none; }
  .contacts li { display: flex; align-items: center; gap: 10px; color: var(--red); font-size: 13px; margin-top: 6px; }
  .contacts svg { width: 14px; height: 14px; flex: none; fill: var(--white); }

  /* Back */
  .back { padding-top: 30px; text-align: center; }
  .pill {
    display: inline-block; background: var(--red); color: var(--white);
    font-weight: 900; border-radius: 4px;
  }
  .services-title { font-size: 13px; padding: 4px 12px; }
  .services {
    margin: 10px 30px 0; font-weight: 700; font-size: 13px; line-height: 1.75;
  }
  .services .dot { color: var(--red); margin: 0 5px; }
  .cta { margin-top: 12px; font-size: 15px; padding: 6px 18px; font-weight: 700; }
  .cta strong { font-weight: 900; font-size: 18px; margin-left: 8px; }
  .notes-label { color: var(--red); font-size: 13px; margin-top: 10px; font-weight: 700; }
  .note-line { height: 0; border-top: 3px dotted var(--dots); margin: 20px 40px 0; }
</style>
</head>
<body>

<section class="card front" aria-label="Business card front">
  <div class="brand">
    <span class="brand-dot"></span>
    <span class="brand-name">Bright Path<br>Electrical &amp; Communication</span>
  </div>
  <p class="tagline">Electrifying Fast Service With Quality Work</p>

  <div class="person">
    <p class="person-name">Dorian Velcourt</p>
    <p class="person-role">MANAGING DIRECTOR</p>
    <p class="licence">EC 27036</p>
    <p class="abn">ABN 52 147 906 318</p>
  </div>

  <ul class="contacts">
    <li>
      <svg viewBox="0 0 16 16" aria-hidden="true"><path d="M3 1h4l1 4-2 1.5a9 9 0 0 0 3.5 3.5L11 8l4 1v4a2 2 0 0 1-2 2A12 12 0 0 1 1 3a2 2 0 0 1 2-2z"/></svg>
      0452681207
    </li>
    <li>
      <svg viewBox="0 0 16 16" aria-hidden="true"><path d="M1 3h14v10H1z M2 4l6 5 6-5" stroke="#2a2a2a" stroke-width="1"/></svg>
      info@ridgewirecrew.com.au
    </li>
    <li>
      <svg viewBox="0 0 16 16" aria-hidden="true"><circle cx="8" cy="8" r="6.5" fill="none" stroke="#f2f2f2" stroke-width="1.4"/><path d="M1.5 8h13M8 1.5c-3 3.5-3 9.5 0 13M8 1.5c3 3.5 3 9.5 0 13" fill="none" stroke="#f2f2f2" stroke-width="1.2"/></svg>
      www.ridgewirecrew.com.au
    </li>
    <li>
      <svg viewBox="0 0 16 16" aria-hidden="true"><path d="M8 1a5 5 0 0 0-5 5c0 4 5 9 5 9s5-5 5-9a5 5 0 0 0-5-5zm0 7a2 2 0 1 1 0-4 2 2 0 0 1 0 4z"/></svg>
      48 Marlow Rd Tandridge Perth 6093
    </li>
  </ul>
</section>

<section class="card back" aria-label="Business card back">
  <span class="pill services-title">OUR SERVICES</span>
  <p class="services">
    Emergency Call Outs<span class="dot">•</span>Repairs<span class="dot">•</span>Safety Switches / RCD<span class="dot">•</span>New Installations<br>
    New Homes<span class="dot">•</span>Smoke Alarms<span class="dot">•</span>Power Points<span class="dot">•</span>Lighting / LED<span class="dot">•</span>Re-Wire<br>
    Switchboard Upgrades<span class="dot">•</span>Ovens<span class="dot">•</span>Range Hoods<span class="dot">•</span>Phone / Data<span class="dot">•</span>Test &amp; Tag
  </p>
  <span class="pill cta">Call Us Today For A Free Quote <strong>0452 681 207</strong></span>
  <p class="notes-label">Notes..</p>
  <div class="note-line"></div>
  <div class="note-line"></div>
  <div class="note-line"></div>
</section>

</body>
</html>
```